Brightvale Circuit

Marion T Hadley
"Title" Adventure Manager & Host
2817 North 9th Street | Vancouver, BC | V5R 2K8
Direct 604.582. 1907 x 215
Chatline drum41
1.800.436.5127
brightvale.ca
(perhaps small steady route bureau logo somewhere? Or “Powered by SRB”?)
- Grey/white logo cut out on reverse of card with web address

Industry/Entity Type

Travel

```html
<!DOCTYPE html>
<html lang="en">
<head>
<meta charset="utf-8">
<title>Brightvale Circuit – Business Card</title>
<link rel="stylesheet" href="https://fonts.googleapis.com/css2?family=Ubuntu:wght@400;500;700&display=swap">
<style>
  :root {
    --page: #ffffff;
    --card-front: #4d4d4d;
    --card-dark: #333333;
    --card-light: #ffffff;
    --accent: #8cc63f;
    --ink-dark: #222222;
    --ink-light: #ffffff;
    --ink-muted: #e6e6e6;
  }
  * { margin: 0; padding: 0; box-sizing: border-box; }
  html, body {
    width: 1200px; height: 900px; overflow: hidden;
    background: var(--page);
    font-family: "Ubuntu", sans-serif;
  }
  .canvas { position: relative; width: 1200px; height: 900px; }

  .card { position: absolute; width: 566px; height: 340px; border-radius: 14px; overflow: hidden; }

  .card--reverse { left: 310px; top: 80px; background: var(--card-front); }
  .card--reverse .brand { position: absolute; left: 0; right: 0; top: 150px; justify-content: center; }

  .brand { display: flex; align-items: center; gap: 12px; }
  .brand__mark { width: 26px; height: 26px; background: var(--accent); }
  .brand__name {
    font-family: "Ubuntu", sans-serif; font-weight: 700; font-size: 30px;
    color: var(--accent); letter-spacing: 0.5px; white-space: nowrap;
  }

  .card--front {
    left: 299px; top: 485px; width: 565px;
    background: var(--card-light);
    box-shadow: 0 4px 8px rgba(0,0,0,0.35);
  }
  .card__shape { position: absolute; inset: 0; }
  .card--front .brand { position: absolute; left: 13px; top: 135px; gap: 10px; }
  .card--front .brand__mark { width: 24px; height: 24px; }
  .card--front .brand__name { font-size: 27px; }

  .holder {
    position: absolute; left: 323px; top: 33px;
    font-weight: 500; font-size: 27px; color: var(--ink-light); letter-spacing: 0.3px;
  }
  .contact {
    position: absolute; left: 323px; top: 186px;
    font-size: 16px; line-height: 21.5px; color: var(--ink-light);
  }
  .contact__web { margin-top: 16px; }
  .powered {
    position: absolute; right: 15px; top: 302px;
    font-size: 13px; color: var(--ink-muted);
  }
  .address {
    position: absolute; left: 13px; top: 254px;
    font-size: 16px; line-height: 22px; color: var(--ink-dark);
  }
</style>
</head>
<body>
<main class="canvas">

  <section class="card card--reverse" aria-label="Card reverse">
    <div class="brand">
      <span class="brand__mark"></span>
      <span class="brand__name">Brightvale Circuit</span>
    </div>
  </section>

  <section class="card card--front" aria-label="Card front">
    <svg class="card__shape" width="565" height="340" viewBox="0 0 565 340" aria-hidden="true">
      <path d="M256,0 C330,90 325,220 186,340 L221,340 C300,240 318,100 261,0 Z" fill="var(--accent)"/>
      <path d="M261,0 C318,100 300,240 221,340 L565,340 L565,0 Z" fill="var(--card-dark)"/>
    </svg>

    <div class="brand">
      <span class="brand__mark"></span>
      <span class="brand__name">Brightvale Circuit</span>
    </div>

    <p class="address">
      Adventure Manager &amp; Host<br>
      2817 North 9th Street |<br>
      Vancouver, BC | V5R 2K8
    </p>

    <h1 class="holder">Marion T Hadley</h1>

    <div class="contact">
      <p>Direct 604.582. 1907 x 215</p>
      <p>Chatline drum41</p>
      <p>1.800.436.5127</p>
      <p class="contact__web">website: www.brightvale.ca</p>
    </div>

    <p class="powered">Powered by SRB</p>
  </section>

</main>
</body>
</html>
```